Business card

would like a double sided business card made up with my logos provided.
Prefer card to have black background and to use the black logos, with matching blue writing for the text.
One side to just be the logo, (Try to use both the black logos)
the other side to have the logo and also my credentials/business information.

Covering all aspects of Carpentry and Building Services

Marcus Tolvey
Qualified Carpenter
Mob: 0417263948
Email: rkt.joinery@mailbright.com
ABN: 47 615 209 834

Industry/Entity Type

Business

Contact Information for Business Card

Marcus Tolvey
Qualified Carpenter
Mob: 0417263948
ABN: 47 615 209 834

Requirements
Must have
• Please try to use both the black logos and incorporate into the card.

```html
<!DOCTYPE html>
<html lang="en">
<head>
<meta charset="utf-8">
<title>RKT Joinery – Business Card</title>
<link rel="stylesheet" href="https://fonts.googleapis.com/css2?family=Lato:wght@400;700;900&display=swap">
<style>
  :root {
    --page-bg: #2b2b2b;
    --card-bg: #1c1c1d;
    --card-edge: #262627;
    --brand-blue: #1a6fb5;
    --text-white: #ececec;
    --text-grey: #bdbdbd;
  }
  * { box-sizing: border-box; margin: 0; padding: 0; }
  html, body {
    width: 1200px;
    height: 997px;
    overflow: hidden;
    background: var(--page-bg);
    font-family: "Lato", sans-serif;
  }
  .card {
    position: absolute;
    width: 560px;
    height: 320px;
    background: var(--card-bg);
    border: 1px solid var(--card-edge);
    border-radius: 22px;
    box-shadow: 0 18px 40px rgba(0,0,0,.45);
  }
  .card--front { left: 70px; top: 110px; }
  .card--back { left: 570px; top: 530px; }

  .brand { display: flex; align-items: center; gap: 12px; }
  .brand__mark { width: 22px; height: 22px; background: var(--brand-blue); }
  .brand__name {
    font-weight: 900;
    color: var(--text-white);
    letter-spacing: .04em;
    line-height: 1;
  }

  /* Front */
  .card--front .front-content {
    position: absolute;
    inset: 0;
    display: flex;
    flex-direction: column;
    align-items: center;
    justify-content: center;
    text-align: center;
  }
  .card--front .brand__name { font-size: 54px; }
  .card--front .brand__mark { width: 30px; height: 30px; }
  .tagline { margin-top: 34px; font-weight: 700; font-size: 15px; letter-spacing: .1em; line-height: 1.5; }
  .tagline__lead { color: var(--text-grey); display: block; }
  .tagline__services { color: var(--brand-blue); display: block; }

  /* Back */
  .card--back .brand { position: absolute; left: 40px; top: 46px; }
  .card--back .brand__name { font-size: 34px; }
  .abn {
    position: absolute;
    right: 40px;
    top: 118px;
    font-weight: 700;
    font-size: 15px;
    color: var(--text-white);
  }
  .abn__label { color: var(--brand-blue); }
  .divider {
    position: absolute;
    left: 250px;
    right: 40px;
    top: 176px;
    height: 2px;
    background: var(--brand-blue);
  }
  .person { position: absolute; left: 40px; top: 160px; }
  .person__name { font-weight: 700; font-size: 20px; color: var(--brand-blue); }
  .person__title { font-weight: 700; font-size: 13px; color: var(--text-white); letter-spacing: .04em; margin-top: 2px; }
  .contact-list { list-style: none; margin-top: 18px; }
  .contact-list__item {
    display: flex;
    align-items: center;
    gap: 14px;
    font-size: 14px;
    color: var(--brand-blue);
    margin-bottom: 12px;
  }
  .contact-list__icon { width: 18px; height: 18px; flex: none; }
</style>
</head>
<body>

<section class="card card--front" aria-label="Business card front">
  <div class="front-content">
    <div class="brand">
      <span class="brand__mark"></span>
      <span class="brand__name">RKT JOINERY</span>
    </div>
    <p class="tagline">
      <span class="tagline__lead">COVERING ALL ASPECTS OF</span>
      <span class="tagline__services">CARPENTRY &amp; BUILDING SERVICES</span>
    </p>
  </div>
</section>

<section class="card card--back" aria-label="Business card back">
  <div class="brand">
    <span class="brand__mark"></span>
    <span class="brand__name">RKT JOINERY</span>
  </div>
  <p class="abn"><span class="abn__label">ABN:</span> 47 615 209 834</p>
  <div class="divider"></div>
  <div class="person">
    <p class="person__name">Marcus Tolvey</p>
    <p class="person__title">QUALIFIED CARPENTER</p>
    <ul class="contact-list">
      <li class="contact-list__item">
        <svg class="contact-list__icon" viewBox="0 0 18 18" aria-hidden="true">
          <rect x="4" y="1" width="10" height="16" rx="2" fill="none" stroke="#ececec" stroke-width="1.6"/>
          <line x1="7.5" y1="14" x2="10.5" y2="14" stroke="#ececec" stroke-width="1.4"/>
        </svg>
        0417263948
      </li>
      <li class="contact-list__item">
        <svg class="contact-list__icon" viewBox="0 0 18 18" aria-hidden="true">
          <rect x="1" y="4" width="16" height="11" fill="#ececec"/>
          <polyline points="1,4 9,10.5 17,4" fill="none" stroke="#1c1c1d" stroke-width="1.4"/>
        </svg>
        rkt.joinery@mailbright.com
      </li>
    </ul>
  </div>
</section>

</body>
</html>
```